Wedding Day Custom Wine Label - Tasmanian (Tamar Valley) wine

I am looking for a custom design that will be put on a wine label to commemorate a very good friend's wedding day.

We will need to be able to take the design and print it on to sticker labels that we can put on to wine bottles.

The bride and groom have asked for a simplistic label design (see example image attached). We need two labels. One for "Pinot Noir" wine and the other for "Chardonnay" wine. We would like the label to say:

The Hartwell's
Pinot Noir
2023
Tamar Valley

and for for the other wine variety:

The Hartwell's
Chardonnay
2023
Tamar Valley

smaller text below to say:

13.5% ALC/VOL 750ML
MEGAN & LIAM - 31.10.2024

I am happy to consider other variations - the bride & groom would prefer something minimalistic. Elegant and classy.

Target Market(s)

the bride & groom

Requirements
Must have
• Wedding date (31.10.2024). Wine type (Pinot Noir or Chardonnay).
Should not have
• images not essential

```html
<!DOCTYPE html>
<html lang="en">
<head>
<meta charset="utf-8">
<title>The Hartwell's – Pinot Noir Wedding Label</title>
<link rel="stylesheet" href="https://fonts.googleapis.com/css2?family=IM+Fell+English+SC&family=Arimo&display=swap">
<style>
  :root {
    --ink: #14233a;
    --paper: #ffffff;
  }
  html, body {
    margin: 0;
    padding: 0;
    overflow: hidden;
    background: var(--paper);
  }
  .canvas {
    width: 1200px;
    height: 704px;
    display: flex;
    align-items: center;
    justify-content: center;
    background: var(--paper);
    overflow: hidden;
  }
  .wine-label {
    height: 640px;
    width: auto;
    display: block;
  }
  .label-display {
    font-family: "IM Fell English SC", Georgia, serif;
    fill: var(--ink);
  }
  .label-estate { font-size: 84px; letter-spacing: 4px; }
  .label-variety { font-size: 58px; letter-spacing: 3px; }
  .label-region { font-size: 58px; letter-spacing: 3px; }
  .label-vintage { font-size: 96px; letter-spacing: 2px; }
  .label-couple { font-size: 42px; letter-spacing: 2px; }
  .label-date { font-size: 38px; letter-spacing: 1px; }
  .label-spec {
    font-family: "Arimo", Arial, sans-serif;
    font-size: 28px;
    fill: var(--ink);
  }
  .label-seal {
    fill: none;
    stroke: var(--ink);
    stroke-width: 10;
  }
</style>
</head>
<body>
<main class="canvas">
  <svg class="wine-label" viewBox="200 300 760 880" xmlns="http://www.w3.org/2000/svg" aria-labelledby="label-title">
    <title id="label-title">The Hartwell's Pinot Noir 2023, Tamar Valley – Megan &amp; Liam, 31.10.2024</title>
    <defs>
      <path id="arc-estate" d="M251,602 A345,345 0 0 1 899,602"/>
      <path id="arc-variety" d="M383,686 A195,195 0 0 1 767,686"/>
      <path id="arc-region" d="M350,802 A240,240 0 0 0 800,802"/>
    </defs>

    <text class="label-display label-estate">
      <textPath href="#arc-estate" startOffset="50%" text-anchor="middle">THE HARTWELL'S</textPath>
    </text>

    <circle class="label-seal" cx="575" cy="720" r="268"/>

    <text class="label-display label-variety">
      <textPath href="#arc-variety" startOffset="50%" text-anchor="middle">PINOT NOIR</textPath>
    </text>

    <text class="label-display label-vintage" x="577" y="752" text-anchor="middle">2023</text>

    <text class="label-display label-region">
      <textPath href="#arc-region" startOffset="50%" text-anchor="middle">TAMAR VALLEY</textPath>
    </text>

    <text class="label-spec" x="240" y="1122">750 ml</text>
    <text class="label-display label-couple" x="577" y="1108" text-anchor="middle">MEGAN &amp; LIAM</text>
    <text class="label-display label-date" x="577" y="1155" text-anchor="middle">31.10.2024</text>
    <text class="label-spec" x="932" y="1122" text-anchor="end">13.5% vol.</text>
  </svg>
</main>
</body>
</html>
```